Pitch book for Birchvale Real Estate Investors.

Birchvale Investors is a new real estate investment company focused on multifamily (apartment) investments along the San Francisco Peninsula (in other parts of the world it is also referred to as flats). We need a professional Pitch Book i.e. brochure (digital and print) to raise equity from private investors. Read about “pitch book” on Wikipedia. The profile of the investor is conservative and must qualify as an accredited investor. Think high net worth individuals, CEOs and wealthy retiring couples. The investor that is attracted to real estate invest because it is low risk, produce cash flow and provide solid returns over the long term.

The brochure should convey trust, be highly professional and be clean and crisp. I attach a PowerPoint doc to be used as a copy for the brochure. I also attach a brochure of Harlow Pike – I like the look and feel, think it was designed with InDesign.

We will use the brochure at one-on-one meetings with investors where we will present on a laptop; we also need it in a format so that we can email it, print it and use it to be uploaded as a website.

I prefer the up and down scroll format (like you would do on a Mac) compared to PowerPoint but I am open to suggestions.

The photos I used in the PowerPoint presentation was found on the web, please use your own stock images.

Target Market(s)

High net worth individuals

Industry/Entity Type

Real Estate

Font styles to use
Serif

Requirements
Must have
• See attached Power Point
Nice to have
• See attached HPK brochure, I like the look and feel.
Should not have
• I am open to your ideas.

```html
<!DOCTYPE html>
<html lang="en">
<head>
<meta charset="utf-8">
<title>Birchvale Investors — Pitch Book Spread</title>
<link rel="stylesheet" href="https://fonts.googleapis.com/css2?family=Jost:wght@300;400;500&family=Open+Sans:wght@600;700&display=swap">
<style>
  :root {
    --backdrop: #8e8e8e;
    --paper: #ffffff;
    --paper-shade: #e9e9e9;
    --ink: #2a2a2a;
    --ink-soft: #3a3a3a;
    --sky-top: #9fb0c2;
    --sky-low: #c4c9cc;
    --city-warm: #a99680;
    --city-shade: #5f5a55;
  }
  * { box-sizing: border-box; margin: 0; padding: 0; }
  html, body {
    width: 1200px; height: 800px; overflow: hidden;
    background: var(--backdrop);
  }
  .spread {
    position: absolute; left: 80px; top: 60px;
    width: 1040px; height: 680px;
    background: var(--paper);
    display: flex;
    box-shadow: 0 6px 18px rgba(0,0,0,0.25);
    font-family: "Jost", "Futura", sans-serif;
    color: var(--ink);
  }
  .page { position: relative; width: 520px; height: 100%; }
  .page--left { background: linear-gradient(to right, var(--paper) 80%, var(--paper-shade)); }
  .page--right { background: linear-gradient(to right, var(--paper-shade), var(--paper) 14%); }

  .running-head {
    position: absolute; top: 14px;
    font-family: "Open Sans", sans-serif;
    line-height: 1.1;
  }
  .running-head__title { font-size: 11px; font-weight: 700; }
  .running-head__sub { font-size: 7px; font-weight: 600; }
  .page--left .running-head { left: 30px; }
  .page--right .running-head { right: 30px; text-align: right; }

  .hero-photo {
    position: absolute; left: 30px; top: 44px;
    width: 980px; height: 300px;
    background:
      linear-gradient(to bottom, var(--sky-top) 0%, var(--sky-low) 35%, transparent 36%),
      linear-gradient(to bottom, #b9b3a8 36%, var(--city-warm) 62%, var(--city-shade) 100%);
    z-index: 1;
  }

  .mission {
    position: absolute; left: 30px; top: 370px; width: 460px;
  }
  .mission__lead {
    font-size: 24px; font-weight: 300; line-height: 1.25;
  }
  .mission__headline {
    margin-top: 26px;
    font-size: 25px; font-weight: 400; letter-spacing: 0.3px;
  }
  .mission__body {
    margin-top: 30px;
    font-size: 12.5px; font-weight: 400; line-height: 1.5;
    color: var(--ink-soft);
  }

  .focus {
    position: absolute; left: 40px; top: 360px; width: 450px;
    font-size: 12.5px; line-height: 1.5; color: var(--ink-soft);
  }
  .focus__question, .focus__label { font-weight: 500; color: var(--ink); }
  .focus__label { margin-top: 18px; }
  .focus__list { margin-top: 2px; padding-left: 22px; }
  .focus__list li { margin-bottom: 1px; }

  .folio {
    position: absolute; font-size: 12px; font-weight: 500;
  }
  .page--left .folio { left: 30px; bottom: 22px; }
  .page--right .folio { right: 30px; top: 510px; }
</style>
</head>
<body>
  <main class="spread">
    <section class="page page--left">
      <header class="running-head">
        <div class="running-head__title">San Francisco Peninsula</div>
        <div class="running-head__sub">Multifamily Real Estate Investment</div>
      </header>

      <div class="hero-photo" role="img" aria-label="Aerial photograph of the downtown San Francisco skyline with high-rise towers and the bay at left, in warm late-afternoon light"></div>

      <div class="mission">
        <p class="mission__lead">Our Mission….<br>to protect and grow your investment</p>
        <h1 class="mission__headline">FIND, BUY, HOLD FOR THE LONG-TERM</h1>
        <p class="mission__body">Birchvale Investors’ core goal is to identify investments that produce consistent cash flow, have long-term value prospects not currently recognized by the market, and once acquired, increase their operational and managerial efficiencies to maximize cash flow and capital appreciation.</p>
      </div>

      <span class="folio">4</span>
    </section>

    <section class="page page--right">
      <header class="running-head">
        <div class="running-head__title">San Francisco Peninsula</div>
        <div class="running-head__sub">Multifamily Real Estate Investment</div>
      </header>

      <div class="focus">
        <p class="focus__question">Why focus on a specific asset class and geography?</p>
        <p>A focused approach is one of our competitive advantages. With 20 years real estate investment and development experience, Birchvale Investors is a Silicon Valley-based multifamily investment and advisory firm, laser-focused on growing cash flow and lasting value for our clients.</p>
        <p class="focus__label">We invest only:</p>
        <ul class="focus__list">
          <li>In existing properties - we can evaluate existing expenses and rent rolls with more certainty;</li>
          <li>In select San Francisco and Silicon Valley locations - we know the streets and neighborhoods;</li>
          <li>Using low risk core and core plus investment strategies - to reasonably predict cash flow; and</li>
          <li>For the long-term - your investment is a safe-haven that endures market fluctuations.</li>
        </ul>
      </div>

      <span class="folio">5</span>
    </section>
  </main>
</body>
</html>
```